Meridel Haulage - Website

A clean, not cluttered informative website for our business. We specialize in the transportation of radioactive materials across North America. The site is mostly for information about our company and will not be used to attract business but will be used to attract employee's mainly drivers. Driver's are very hard to find in our area. One of the pages needs to be a job's posting page with an apply now button. Either an application can be filled out there or a resume can be uploaded which ever functionality works better. I would like a website that I can easily edit, ability to change text and photos.

Number of Pages Required

5+ page

Colors

Designer to choose colors to be used in the design.

Requirements
Must have
• Home - About - Services - Jobs - Contact pages
• A way prospective employee's can apply or upload their resume to be emailed to me
• Very clean apperance
Should not have
• I don't want it to be busy

```html
<!DOCTYPE html>
<html lang="en">
<head>
<meta charset="utf-8">
<title>Meridel Haulage</title>
<link href="https://fonts.googleapis.com/css2?family=Montserrat:wght@400;600;700;800&family=Open+Sans:wght@400;600&display=swap" rel="stylesheet">
<style>
:root{
  --red:#e3262b;
  --red-dark:#b9141b;
  --red-soft:#f04a48;
  --ink:#2a2a2a;
  --body:#555;
  --muted:#8a8a8a;
  --light:#f4f4f4;
  --white:#fff;
  --line:#e2e2e2;
}
*{box-sizing:border-box;margin:0;padding:0}
html,body{width:1200px;height:4748px;overflow:hidden}
body{font-family:"Open Sans",Arial,sans-serif;color:var(--body);background:var(--white);position:relative;font-size:15px;line-height:1.7}
.section{position:absolute;left:0;width:1200px}
h1,h2,h3,h4,.brand,.nav,.btn{font-family:"Montserrat",Arial,sans-serif}
.btn{display:inline-block;background:var(--red);color:#fff;font-weight:700;font-size:15px;padding:12px 40px;border-radius:26px;text-decoration:none}
.brand{font-weight:800;color:var(--red);letter-spacing:1px;text-transform:uppercase;display:flex;align-items:center;gap:10px}
.brand .dot{width:14px;height:14px;border-radius:50%;background:var(--red)}

/* header */
.site-header{top:0;height:120px;background:var(--white);z-index:3}
.site-header .brand{position:absolute;left:36px;top:38px;font-size:30px}
.topbar{position:absolute;right:40px;top:14px;display:flex;gap:26px;font-size:13px;color:var(--body);align-items:center}
.topbar span{display:flex;align-items:center;gap:6px}
.topbar .social{display:flex;gap:6px}
.topbar .social i{width:18px;height:18px;background:var(--red);border-radius:3px;display:block}
.nav{position:absolute;right:40px;top:58px;display:flex;gap:30px;font-size:15px;font-weight:700;color:var(--ink);list-style:none}
.nav li{padding:8px 14px;border-radius:20px}
.nav li.active{background:var(--red);color:#fff}
.hero{top:120px;height:560px;background:linear-gradient(180deg,#d9dde1 0%,#b7bcc2 55%,#8e9297 100%)}

/* intro */
.intro{top:680px;height:620px}
.intro h2{position:absolute;left:80px;top:50px;width:1040px;font-size:26px;font-weight:800;color:var(--ink);text-transform:uppercase;line-height:1.35}
.intro h2 em{font-style:normal;color:var(--red)}
.map{position:absolute;left:80px;top:130px;width:520px;height:420px;background:linear-gradient(180deg,#3f68c9 0%,#3b63c2 50%,#d62a2a 60%,#c91f22 100%);border-radius:40px 80px 30px 60px}
.intro .copy{position:absolute;left:640px;top:150px;width:480px}
.intro .copy p{margin-bottom:20px}

/* about */
.about{top:1300px;height:480px;background:var(--light);text-align:center}
.section-title{display:inline-flex;align-items:center;gap:12px;font-size:26px;font-weight:800;color:var(--ink);text-transform:uppercase}
.section-title em{font-style:normal;color:var(--red)}
.about .section-title{margin-top:110px}
.about p{width:1000px;margin:28px auto 34px}

/* services */
.services{top:1780px;height:860px;background:linear-gradient(160deg,var(--red-soft) 0%,var(--red) 45%,var(--red-dark) 100%);clip-path:polygon(0 0,100% 0,100% 88%,50% 100%,0 88%);color:#fff;text-align:center}
.services .section-title{color:#fff;margin-top:80px}
.services .lead{width:1000px;margin:24px auto 0;font-size:15px}
.hub{position:absolute;left:450px;top:270px;width:300px;height:300px;border-radius:50%;background:rgba(255,255,255,.18);display:flex;align-items:center;justify-content:center}
.hub .inner{width:240px;height:240px;border-radius:50%;background:#fff;display:flex;align-items:center;justify-content:center}
.hub .brand{font-size:22px}
.service{position:absolute;display:flex;align-items:center;gap:14px;font-family:"Montserrat",sans-serif;font-weight:600;font-size:17px;text-align:left}
.service .icon{width:72px;height:72px;border-radius:50%;background:#fff;display:flex;align-items:center;justify-content:center;flex:none}
.service.right{flex-direction:row-reverse;text-align:right}
.s1{left:60px;top:290px}.s2{left:60px;top:470px}.s3{right:60px;top:290px}.s4{right:60px;top:470px}
.links{position:absolute;left:0;top:0}

/* join */
.join{top:2640px;height:380px}
.join .section-title{position:absolute;left:80px;top:0}
.join p{position:absolute;left:80px;top:56px;width:470px}
.join .btn{position:absolute;left:80px;top:280px}
.join-photo{position:absolute;left:600px;top:-150px;width:520px;height:500px;background:linear-gradient(180deg,#cfd4da 0%,#9aa1a9 60%,#6e757c 100%)}

/* news */
.news{top:3020px;height:600px;text-align:center}
.news .section-title{margin-top:30px}
.cards{position:absolute;left:88px;top:120px;display:flex;gap:46px}
.card{width:320px;height:400px;background:#fff;box-shadow:0 4px 18px rgba(0,0,0,.12);text-align:left}
.card .thumb{height:170px}
.t1{background:linear-gradient(180deg,#e9a25b,#3f4a5a)}
.t2{background:linear-gradient(180deg,#4d86c7,#1f3552)}
.t3{background:linear-gradient(180deg,#8fb4d8,#8a8f95)}
.card .body{padding:18px 22px}
.card .date{display:flex;align-items:center;gap:8px;font-size:13px;color:var(--muted);border-bottom:1px solid var(--line);padding-bottom:8px;margin-bottom:10px}
.card .date i{width:16px;height:16px;border:2px solid var(--red);border-radius:2px}
.card h4{font-size:15px;color:var(--ink);font-weight:600;line-height:1.4}
.card p{font-size:13px;margin-top:6px}
.card a{display:block;color:var(--red);font-size:13px;margin-top:14px;text-decoration:none}

/* contact */
.contact{top:3620px;height:600px;background:linear-gradient(180deg,#e8403f 0%,#c92125 60%,#a3161b 100%);clip-path:polygon(0 0,50% 10%,100% 0,100% 100%,0 100%);text-align:center;color:#fff}
.contact .section-title{color:#fff;margin-top:110px}
.contact h3{font-size:15px;font-weight:700;text-transform:uppercase;margin-top:14px}
.form{position:absolute;left:80px;top:220px;width:1040px}
.form .row{display:flex;gap:20px}
.field{flex:1;height:44px;background:rgba(0,0,0,.22);text-align:left;padding:10px 16px;font-size:13px}
.field.msg{height:150px;margin-top:20px}
.contact .send{background:#fff;color:var(--red);margin-top:30px}

/* footer */
.site-footer{top:4220px;height:528px;background:#fff}
.site-footer .brand{justify-content:center;font-size:30px;margin-top:50px}
.cols{position:absolute;left:60px;top:160px;width:1080px;display:flex;gap:30px}
.col{flex:1;font-size:13px}
.col h4{color:var(--red);font-size:13px;font-weight:700;text-transform:uppercase;border-bottom:1px solid var(--line);padding-bottom:8px;margin-bottom:10px}
.col li{list-style:none;line-height:1.8;display:flex;align-items:center;gap:8px}
.col li i{width:18px;height:18px;border-radius:50%;background:var(--red);display:inline-block;flex:none}
.col .email{border:1px solid var(--line);padding:8px;margin-top:10px;color:var(--muted)}
.col .sub{display:inline-block;background:var(--red);color:#fff;font-weight:700;padding:6px 18px;border-radius:14px;margin-top:10px;font-family:"Montserrat",sans-serif;font-size:12px}
.copyright{position:absolute;left:0;bottom:0;width:1200px;height:32px;background:var(--red);color:#fff;font-size:12px;text-align:center;line-height:32px}
</style>
</head>
<body>

<header class="section site-header">
  <div class="brand">Meridel Haulage</div>
  <div class="topbar">
    <span><svg width="14" height="14" viewBox="0 0 24 24"><path fill="#e3262b" d="M6.6 10.8a15 15 0 0 0 6.6 6.6l2.2-2.2a1 1 0 0 1 1-.25 11 11 0 0 0 3.6.6 1 1 0 0 1 1 1V20a1 1 0 0 1-1 1A17 17 0 0 1 3 4a1 1 0 0 1 1-1h3.5a1 1 0 0 1 1 1 11 11 0 0 0 .6 3.6 1 1 0 0 1-.25 1z"/></svg>(555) 014-2290</span>
    <span><svg width="14" height="14" viewBox="0 0 24 24"><rect x="2" y="5" width="20" height="14" rx="2" fill="#e3262b"/><path d="M2 6l10 7 10-7" stroke="#fff" stroke-width="2" fill="none"/></svg>hello@meridelhaulage.com</span>
    <span class="social"><i></i><i></i><i></i></span>
  </div>
  <ul class="nav">
    <li class="active">HOME</li><li>ABOUT</li><li>SERVICES</li><li>JOBS</li><li>NEWS</li><li>CONTACT</li>
  </ul>
</header>

<div class="section hero" role="img" aria-label="Photo of a tanker truck hauling a container past cooling towers, with yellow hazard barrels in front"></div>

<section class="section intro">
  <h2>Meridel Haulage has been the leader in the <em>transportation of radioactive materials</em> across North America since 1980</h2>
  <div class="map" role="img" aria-label="Map of North America with the United States highlighted in red and Canada in blue"></div>
  <div class="copy">
    <p>Lorem ipsum dolor sit amet, consectetur adipiscing elit, sed do eiusmod tempor incididunt ut labore et dolore magna aliqua. Ut enim ad minim veniam, quis nostrud exercitation ullamco laboris nisi ut aliquip ex ea commodo consequat.</p>
    <p>Duis aute irure dolor in reprehenderit in voluptate velit esse cillum dolore eu fugiat nulla pariatur. Excepteur sint occaecat cupidatat non proident, sunt in culpa qui officia deserunt mollit anim id est laborum.</p>
  </div>
</section>

<section class="section about">
  <h2 class="section-title"><svg width="40" height="20" viewBox="0 0 40 20"><path d="M2 16 Q20 -4 38 10" stroke="#e3262b" stroke-width="3" fill="none"/></svg>About <em>Meridel Haulage</em></h2>
  <p>Lorem ipsum dolor sit amet, consectetur adipiscing elit, sed do eiusmod tempor incididunt ut labore et dolore magna aliqua. Ut enim ad minim veniam, quis nostrud exercitation ullamco laboris nisi ut aliquip ex ea commodo consequat. Duis aute irure dolor in reprehenderit in voluptate velit esse cillum dolore eu fugiat nulla pariatur. Excepteur sint occaecat cupidatat non proident, sunt in culpa qui officia deserunt mollit anim id est laborum.</p>
  <a class="btn">Learn More</a>
</section>

<section class="section services">
  <h2 class="section-title"><svg width="40" height="20" viewBox="0 0 40 20"><path d="M2 16 Q20 -4 38 10" stroke="#fff" stroke-width="3" fill="none"/></svg>Our Services</h2>
  <p class="lead">We are here to manage your logistical needs from start to finish, and our extensive experience allows us to offer innovative, reliable, and safe front-end and nuclear transportation solutions for the following materials:</p>
  <svg class="links" width="1200" height="860" viewBox="0 0 1200 860">
    <g stroke="#fff" stroke-width="2" fill="none" opacity=".8">
      <path d="M330 326 H460"/><path d="M870 326 H740"/>
      <path d="M420 506 H470"/><path d="M780 506 H730"/>
      <circle cx="460" cy="326" r="6" fill="#fff"/><circle cx="740" cy="326" r="6" fill="#fff"/>
      <circle cx="470" cy="506" r="6" fill="#fff"/><circle cx="730" cy="506" r="6" fill="#fff"/>
    </g>
  </svg>
  <div class="hub"><div class="inner"><div class="brand">Meridel Haulage</div></div></div>
  <div class="service s1"><span class="icon"><svg width="36" height="36" viewBox="0 0 36 36"><circle cx="18" cy="18" r="15" fill="none" stroke="#e3262b" stroke-width="3"/><circle cx="18" cy="18" r="4" fill="#e3262b"/></svg></span>Uranium ore concentrate</div>
  <div class="service s2"><span class="icon"><svg width="36" height="36" viewBox="0 0 36 36"><rect x="9" y="6" width="18" height="26" rx="3" fill="#e3262b"/></svg></span>Natural and enriched uranium<br>hexafluoride</div>
  <div class="service right s3"><span class="icon"><svg width="36" height="36" viewBox="0 0 36 36"><rect x="7" y="8" width="22" height="20" rx="2" fill="none" stroke="#e3262b" stroke-width="3"/><path d="M7 22 L15 15 L21 20 L29 13" stroke="#e3262b" stroke-width="3" fill="none"/></svg></span>Uranium Waste</div>
  <div class="service right s4"><span class="icon"><svg width="36" height="36" viewBox="0 0 36 36"><path d="M18 4 C10 16 9 20 9 23 a9 9 0 0 0 18 0 c0-3-1-7-9-19z" fill="#e3262b"/></svg></span>Fuel pellets<br>and bundles</div>
</section>

<section class="section join">
  <h2 class="section-title"><svg width="40" height="20" viewBox="0 0 40 20"><path d="M2 16 Q20 -4 38 10" stroke="#e3262b" stroke-width="3" fill="none"/></svg>Join <em>Meridel</em> Team</h2>
  <p>Lorem ipsum dolor sit amet, consectetur adipiscing elit, sed do eiusmod tempor incididunt ut labore et dolore magna aliqua. Ut enim ad minim veniam, quis nostrud exercitation ullamco laboris nisi ut aliquip ex ea commodo consequat. Duis aute irure dolor in reprehenderit in voluptate velit esse cillum dolore eu fugiat nulla pariatur excepteur sint occaecat cupi.</p>
  <a class="btn">Apply Now</a>
  <div class="join-photo" role="img" aria-label="Photo of a driver standing in front of a row of parked white trucks"></div>
</section>

<section class="section news">
  <h2 class="section-title"><svg width="40" height="20" viewBox="0 0 40 20"><path d="M2 16 Q20 -4 38 10" stroke="#e3262b" stroke-width="3" fill="none"/></svg>Latest <em>News</em></h2>
  <div class="cards">
    <article class="card"><div class="thumb t1" role="img" aria-label="Photo of a power plant at sunset"></div><div class="body"><div class="date"><i></i>Jun 19, 2019</div><h4>Duis aute irure dolor in reprehen</h4><p>Lorem ipsum dolor sit amet, cons ectetur adipiscing elit, sed do eius mod tempor incididunt.</p><a>Read more...</a></div></article>
    <article class="card"><div class="thumb t2" role="img" aria-label="Photo of a city skyline at dusk"></div><div class="body"><div class="date"><i></i>Jun 17, 2019</div><h4>Duis aute irure dolor in reprehen</h4><p>Lorem ipsum dolor sit amet, cons ectetur adipiscing elit, sed do eius mod tempor incididunt.</p><a>Read more...</a></div></article>
    <article class="card"><div class="thumb t3" role="img" aria-label="Photo of industrial cooling towers"></div><div class="body"><div class="date"><i></i>Jun 14, 2019</div><h4>Duis aute irure dolor in reprehen</h4><p>Lorem ipsum dolor sit amet, cons ectetur adipiscing elit, sed do eius mod tempor incididunt.</p><a>Read more...</a></div></article>
  </div>
</section>

<section class="section contact" role="img" aria-label="Red-tinted photo of stacked hazard barrels behind the contact form">
  <h2 class="section-title"><svg width="40" height="20" viewBox="0 0 40 20"><path d="M2 16 Q20 -4 38 10" stroke="#fff" stroke-width="3" fill="none"/></svg>Contact Us</h2>
  <h3>Let us know what you need</h3>
  <div class="form">
    <div class="row"><div class="field">Your Name</div><div class="field">Your Email</div><div class="field">Your Subject</div></div>
    <div class="field msg">Message</div>
    <a class="btn send">Send Message</a>
  </div>
</section>

<footer class="section site-footer">
  <div class="brand">Meridel Haulage</div>
  <div class="cols">
    <div class="col"><h4>Quick Links</h4><ul><li>Home</li><li>About</li><li>Services</li><li>Jobs</li><li>Contact</li></ul></div>
    <div class="col"><h4>Transport Services</h4><ul><li>Uranium ore concentrate</li><li>Uranium hexafluoride</li><li>Uranium waste</li><li>Fuel pellets and bundles</li></ul></div>
    <div class="col"><h4>Contact</h4><ul><li><i></i>Meridel Haulage<br>Harlow Bend, ST 00412</li><li><i></i>(555) 014-2290</li><li><i></i>hello@meridelhaulage.com</li></ul></div>
    <div class="col"><h4>Follow Us</h4><ul><li><i></i>Community</li><li><i></i>Updates</li><li><i></i>Gallery</li></ul></div>
    <div class="col"><h4>Newsletter</h4><p>Register your email address to get our latest news.</p><div class="email">Email Address</div><span class="sub">SUBSCRIBE</span></div>
  </div>
  <div class="copyright">Copyright © 2019 Meridel Haulage. All rights reserved.</div>
</footer>

</body>
</html>
```